6.5x9" Postcard Project for Organic and Sustainably powered Lawn Care Service

Hello,

Looking for a 6.6"Hx9"W postcard for my first direct mail project.

We are a full service lawn care company providing organic lawn treatment programs and full service lawn maintenance with solar powered electric equipment (and sometimes propane/biodiesel equipment for larger lawns and spaces). We are brand new to Houston and are in the midst of our rollout. This will be our first structured marketing effort so we want something that will grab people's attention as well as really do a good job telling people what we're about!

I have some logos and designs from some other products from the other franchisees and was wanting something similar.

Some of our info and "catch phrases":

Site: www.BrightFernYardWorksTexan.com

Phone Number: 713.580.2143

"The Neighborhood's Healthiest Lawn"

"Changing The Way America Mows The Lawn"

"Come Clean"

"Clean. Green. Organic."
If at all possible please include standard every day direct mail indicia as well.

Please let me know if there is anything else I can do to assist making the best product possible.

Thanks!

Marcus

Target Market(s)

Organic and Environmentally Minded people needing lawn service.

Industry/Entity Type

Lawn Care

Requirements
Must have
• Logo, website, phone number, invitation for free estimate

```html
<!DOCTYPE html>
<html lang="en">
<head>
<meta charset="utf-8">
<title>Bright Fern Yard Works – Postcard</title>
<link rel="stylesheet" href="https://fonts.googleapis.com/css2?family=Open+Sans:wght@600;700;800&display=swap">
<style>
  :root{
    --green:#4c7340;
    --green-dark:#2b4a30;
    --green-head:#4a7a3a;
    --white:#ffffff;
    --page:#ffffff;
    --grass-sun:#a6cf5a;
    --grass-light:#7fb23c;
    --grass-mid:#5e9a2a;
    --grass-deep:#3f7420;
    --lawn-sun:#b5c95e;
    --lawn-light:#9bb545;
    --lawn-deep:#7b9632;
    --mascot-brown:#8b5a2b;
    --mascot-tan:#c9a06a;
    --mascot-yellow:#f2cf45;
    --mascot-green:#5aa532;
  }
  *{margin:0;padding:0;box-sizing:border-box}
  html,body{width:1200px;height:1000px;overflow:hidden;background:var(--page)}
  body{font-family:"Open Sans",Arial,sans-serif;position:relative}
  .postcard{position:absolute;left:257px;top:24px;width:688px;height:952px;background:var(--white);outline:2px solid var(--green);overflow:hidden}
  .shapes{position:absolute;left:0;top:0;width:688px;height:952px;z-index:2;pointer-events:none}
  .photo{position:absolute;left:302px;width:386px}
  .photo--child{top:249px;height:357px;
    background:
      radial-gradient(ellipse 60% 45% at 62% 52%,rgba(60,90,40,.35),transparent 70%),
      radial-gradient(ellipse 80% 60% at 20% 15%,var(--grass-sun),transparent 70%),
      linear-gradient(165deg,var(--grass-light) 0%,var(--grass-mid) 55%,var(--grass-deep) 100%);
    clip-path:polygon(0 0,100% 0,100% 303px,0 355px)}
  .photo--clippings{top:554px;height:268px;
    background:
      radial-gradient(ellipse 35% 30% at 78% 62%,rgba(110,90,50,.45),transparent 75%),
      radial-gradient(ellipse 90% 70% at 30% 30%,var(--lawn-sun),transparent 75%),
      linear-gradient(170deg,var(--lawn-light),var(--lawn-deep));
    clip-path:polygon(0 54px,100% 2px,100% 100%,0 100%)}
  .brand{position:absolute;left:40px;top:90px;width:230px;z-index:3;text-align:center;color:var(--white);font-weight:800;font-size:36px;line-height:42px}
  .values{position:absolute;left:43px;top:207px;z-index:3;color:var(--white);font-weight:700;font-size:21px;letter-spacing:.2px}
  .headline{position:absolute;right:32px;top:42px;z-index:3;text-align:right;color:var(--green-head);font-weight:700;line-height:1}
  .headline .the{font-size:27px;display:block}
  .headline .hood{font-size:25px;display:block;margin-top:2px}
  .headline .healthiest{font-size:39px;display:block;margin-top:2px}
  .headline .lawn{font-size:64px;display:block;margin-top:2px}
  .offer{position:absolute;left:37px;top:262px;color:var(--green-dark);font-weight:700;line-height:1.05}
  .offer .big{font-size:40px}
  .offer .small{font-size:27px}
  .benefits{position:absolute;left:41px;top:360px;width:240px;list-style:none;color:var(--green-dark);font-weight:700;font-size:16.5px;line-height:24px}
  .benefits li{position:relative;padding-left:27px;margin-bottom:12px}
  .benefits li svg{position:absolute;left:0;top:6px}
  .mascot{position:absolute;left:40px;top:718px;width:185px;height:152px;z-index:3;
    border:6px solid var(--white);border-radius:46% 46% 38% 38%;
    background:
      radial-gradient(ellipse 30% 28% at 58% 30%,var(--mascot-tan),transparent 80%),
      radial-gradient(ellipse 35% 30% at 60% 72%,var(--mascot-yellow),transparent 80%),
      linear-gradient(180deg,var(--mascot-brown) 0%,var(--mascot-brown) 18%,var(--mascot-green) 55%,var(--mascot-green) 100%);
    box-shadow:0 0 0 1px rgba(0,0,0,.08)}
  .bubble{position:absolute;left:60px;top:872px;z-index:4}
  .bubble span{position:absolute;left:0;top:0;width:158px;height:38px;line-height:38px;text-align:center;color:var(--green);font-weight:700;font-size:19px}
  .band{position:absolute;left:0;top:822px;width:688px;height:130px;background:var(--green)}
  .contact{position:absolute;right:32px;z-index:3;color:var(--white);font-weight:700;text-align:right}
  .contact--phone{top:848px;font-size:31px;display:flex;align-items:center;gap:10px}
  .contact--web{top:893px;font-size:21.5px}
</style>
</head>
<body>
<main class="postcard">
  <div class="photo photo--child" role="img" aria-label="Photo of a young child crouching on a sunny green lawn"></div>
  <div class="photo photo--clippings" role="img" aria-label="Photo of a freshly mown lawn with a wheelbarrow of grass clippings"></div>

  <svg class="shapes" viewBox="0 0 688 952" aria-hidden="true">
    <polygon points="0,0 335,0 471,249 0,249" fill="var(--green)"/>
    <polygon points="335,0 688,0 688,268 481,268" fill="var(--white)"/>
  </svg>

  <div class="brand">Bright Fern<br>Yard Works</div>
  <p class="values">CLEAN | ORGANIC | RENEWABLE</p>

  <h1 class="headline">
    <span class="the">The</span>
    <span class="hood">Neighborhood's</span>
    <span class="healthiest">Healthiest</span>
    <span class="lawn">LAWN</span>
  </h1>

  <h2 class="offer"><span class="big">Invitation</span> <span class="small">for</span><br><span class="small">free</span> <span class="big">Estimate</span></h2>

  <ul class="benefits">
    <li><svg width="14" height="12" viewBox="0 0 14 12"><path d="M1 6h10M7 2l4 4-4 4" stroke="var(--green-dark)" stroke-width="2.4" fill="none"/></svg>Organic treatment programs to ensure your lawn is beautiful and safe for children, pets, and our local environment.</li>
    <li><svg width="14" height="12" viewBox="0 0 14 12"><path d="M1 6h10M7 2l4 4-4 4" stroke="var(--green-dark)" stroke-width="2.4" fill="none"/></svg>Clean and quiet electric equipment powered by renewable resources.</li>
    <li><svg width="14" height="12" viewBox="0 0 14 12"><path d="M1 6h10M7 2l4 4-4 4" stroke="var(--green-dark)" stroke-width="2.4" fill="none"/></svg>Lawn care practices that maximize water conservation and nutrient uptake.</li>
  </ul>

  <div class="band"></div>

  <div class="mascot" role="img" aria-label="Illustrated brand mascot character in a green cape"></div>

  <div class="bubble">
    <svg width="160" height="56" viewBox="0 0 160 56" aria-hidden="true">
      <path d="M6 1h146a5 5 0 0 1 5 5v27a5 5 0 0 1-5 5h-28l32 13-52-13H6a5 5 0 0 1-5-5V6a5 5 0 0 1 5-5z" fill="var(--white)" stroke="var(--green-dark)" stroke-width="1.5"/>
    </svg>
    <span>Come &amp; Clean</span>
  </div>

  <p class="contact contact--phone">
    <svg width="26" height="26" viewBox="0 0 26 26" aria-hidden="true"><circle cx="13" cy="13" r="11.5" fill="none" stroke="var(--white)" stroke-width="2"/><path d="M10 6c-2 1-2 3-1 6s3 6 5 7c1 .5 2 0 3-1l-2-3-2 1c-1-1-2-3-2-5l2-1-1-4z" fill="var(--white)"/></svg>
    713.580.2143
  </p>
  <p class="contact contact--web">www.BrightFernYardWorksTexan.com</p>
</main>
</body>
</html>
```